New Invitation Design Project

We are looking for someone to design our e-vite, save the date and wine labels for our upcoming event on June 26th. Our event is an open house for our current clients and business colleagues to show our appreciation for them. We want to incorporate our new logo. We would like a professional but fun invitation with multiple versions in different manners of the design we choose.

Industry/Entity Type

House

```html
<!DOCTYPE html>
<html lang="en">
<head>
<meta charset="utf-8">
<title>Open House Invitations</title>
<link rel="stylesheet" href="https://fonts.googleapis.com/css2?family=Arvo:wght@400;700&family=Questrial&family=Raleway:ital,wght@1,300&display=swap">
<style>
  :root {
    --slate: #454f55;
    --blue: #4471b8;
    --blue-soft: #6b96d0;
    --green: #a2cb3a;
    --white: #ffffff;
    --mist: #d9dde0;
    --ink: #1a1a1a;
    --page: #ffffff;
  }
  * { box-sizing: border-box; margin: 0; padding: 0; }
  html, body { width: 1000px; height: 1200px; overflow: hidden; background: var(--page); }
  .canvas { position: relative; width: 1000px; height: 1200px; }

  .card { position: absolute; left: 161px; width: 677px; overflow: hidden; background: var(--slate); }
  .card--save { top: 0; height: 580px; }
  .card--invite { top: 620px; height: 580px; }

  .stripe { position: absolute; background: var(--blue); right: 0; }
  .stripe--base { left: 0; }

  .footer-band { position: absolute; left: 0; right: 0; background: var(--green); color: var(--white);
    font-family: "Questrial", sans-serif; text-align: center; }
  .edge { position: absolute; left: 0; right: 0; bottom: 0; height: 10px; background: var(--ink); }

  .badge { position: absolute; width: 184px; height: 184px; border-radius: 50%; background: var(--white);
    display: flex; align-items: center; justify-content: center; text-align: center; }
  .badge__name { font-family: "Questrial", sans-serif; color: var(--slate); font-size: 19px; line-height: 1.25; }

  .art { position: absolute; border-radius: 40px 40px 6px 6px; }
  .art--glass { background: var(--white); border-radius: 30px 30px 4px 4px; opacity: .9; }
  .art--blue { background: var(--blue-soft); }
  .art--green { background: var(--green); }

  .year { position: absolute; font-family: "Arvo", serif; font-weight: 700; color: var(--white); font-size: 42px; letter-spacing: 1px; }

  .headline { position: absolute; font-family: "Raleway", sans-serif; font-style: italic; font-weight: 300;
    color: var(--green); font-size: 42px; letter-spacing: 1px; white-space: nowrap; }

  .details { position: absolute; white-space: nowrap; }
  .details--right { right: 290px; text-align: right; }
  .details--center { left: 52px; width: 360px; text-align: center; }
  .firm { font-family: "Questrial", sans-serif; color: var(--mist); font-size: 21px; line-height: 28px; }
  .event { font-family: "Arvo", serif; font-weight: 700; font-size: 28px; line-height: 34px; letter-spacing: 1px; }
  .when { font-family: "Arvo", serif; color: var(--white); font-size: 19px; line-height: 26px; }
  .when--bold { font-weight: 700; }
  .where { position: absolute; font-family: "Questrial", sans-serif; color: var(--white); font-size: 21px; line-height: 27px; text-align: center; }
</style>
</head>
<body>
<main class="canvas">

  <section class="card card--save">
    <div class="stripe" style="top:33px;height:25px;left:240px"></div>
    <div class="stripe" style="top:103px;height:27px;left:200px"></div>
    <div class="stripe" style="top:165px;height:27px;left:200px"></div>
    <div class="stripe" style="top:226px;height:25px;left:240px"></div>
    <div class="stripe stripe--base" style="top:392px;height:66px"></div>

    <div class="badge" style="left:153px;top:48px"><span class="badge__name">Hartwell<br>Brooks Carver</span></div>

    <div class="art art--glass" role="img" aria-label="Wine glass illustration made of bubbles" style="left:397px;top:275px;width:52px;height:135px"></div>
    <div class="art art--blue" role="img" aria-label="Small wine bottle illustration made of blue bubbles" style="left:460px;top:160px;width:74px;height:252px"></div>
    <div class="art art--green" role="img" aria-label="Large wine bottle illustration made of green bubbles" style="left:540px;top:12px;width:124px;height:400px"></div>
    <div class="year" style="left:539px;top:358px">2014</div>

    <div class="headline" style="left:30px;top:270px">SAVE THE DATE!</div>
    <div class="details details--right" style="top:316px">
      <div class="firm">HARTWELL BROOKS CARVER, LLC</div>
      <div class="event" style="color:var(--white)">OPEN HOUSE</div>
      <div class="when when--bold">June 26, 2014</div>
      <div class="when when--bold" style="padding-right:36px">3-7 pm</div>
    </div>

    <div class="footer-band" style="top:458px;height:112px;padding-top:28px;font-size:21px;line-height:29px">
      RSVP rsvp@hbclegal.com or 555-210-4400<br>
      1200 Meadowbrook Rd, Suite 210, Fairview, IL
    </div>
    <div class="edge"></div>
  </section>

  <section class="card card--invite">
    <div class="stripe" style="top:33px;height:25px;left:240px"></div>
    <div class="stripe" style="top:103px;height:27px;left:200px"></div>
    <div class="stripe" style="top:165px;height:27px;left:200px"></div>
    <div class="stripe" style="top:226px;height:25px;left:240px"></div>
    <div class="stripe stripe--base" style="top:405px;height:62px"></div>

    <div class="badge" style="left:153px;top:62px"><span class="badge__name">Hartwell<br>Brooks Carver</span></div>

    <div class="art art--glass" role="img" aria-label="Wine glass illustration made of bubbles" style="left:397px;top:277px;width:52px;height:135px"></div>
    <div class="art art--blue" role="img" aria-label="Small wine bottle illustration made of blue bubbles" style="left:460px;top:160px;width:74px;height:252px"></div>
    <div class="art art--green" role="img" aria-label="Large wine bottle illustration made of green bubbles" style="left:540px;top:12px;width:124px;height:400px"></div>
    <div class="year" style="left:539px;top:372px">2014</div>

    <div class="details details--center" style="top:249px">
      <div class="firm">HARTWELL BROOKS CARVER, LLC</div>
      <div class="event" style="color:var(--green)">OPEN HOUSE</div>
      <div class="when">June 26, 2014</div>
      <div class="when">3-7pm</div>
    </div>
    <div class="where" style="left:52px;width:360px;top:396px">1200 Meadowbrook Rd, Suite 210<br>Fairview, IL</div>

    <div class="footer-band" style="top:482px;height:88px;padding-top:24px">
      <div style="font-size:21px;line-height:28px">RSVP rsvp@hbclegal.com or 555-210-4400</div>
      <div style="font-size:15px;line-height:24px">hbclegal.com</div>
    </div>
    <div class="edge"></div>
  </section>

</main>
</body>
</html>
```